4 Information One pagers needed for Australia's biggest Oil & Gas Conference

KVR is a global organisation with its corporate headquarters located in Perth, Western Australia and regional offices in Brisbane, Darwin, Singapore, Korea & China.
KVR delivers dedicated project support services, incorporating but not limited to; project design, procurement, construction, installation, commissioning, operations and maintenance. Our cross industry expertise, project expertise and track record of successfully delivering international projects with blue chip clients and partners has led to our fast evolving reputation as a preferred supplier worldwide within the oil and gas industry onshore and offshore within both greenfield and brownfield scopes.

Need to get information on a one page handout. There are 4 documents that need to be developed.

We need a banner across the top and bottom of each page, which has our logo, title of the document, and our contact details (Head Office – Address: Unit 17, 46-48 Marlow Lane, Perth WA 6000 Australia. Phone: +61 8 9371 5086) Needs to keep with the KVR colours but use images that are relevant to the oil and gas/commissioning industries. Our previous “who we are” flyer is attached so you have a feel for what we are after.

Page 1: KVR’ service offerings include (for each take brief paragraph from document attached for description of each. If unable to find information please contact us or search on www.brenvatek.com):
• Engineering Design;
• Construction Management;
• Commissioning (Systems, Processes, Resources);
• Completions Strategy;
• Multi-Disciplinary Engineering;
• Multi-Disciplinary Technicians;
• Operations & Maintenance Support;
• EX Inspect & Maintain;
• On Site Nitrogen Production;
• Water Treatment;
• Compact Separation Systems;
• Processes to support services;
o Technology to improve efficiency and productivity (Finishline Relay, TW Relay).

Page 2: Our Team – please complete in order listed below and images are attached
Derek Halvorsen
Chief Executive Officer (CEO)
An extensively experienced and practical executive in the engineering industry with over 20 years’ service, more specifically in the oil and gas sector, since 1988.
The experience has been gained through a wide array of projects throughout Australia and Overseas working in the area of Design, System Analysing, Commissioning and Construction before commencing in Business Development and then finally Company Management and Directorships.
Derek has gained extensive experience in line and project management roles and more particularly in change management, people development and team motivation.
He has extensive experience leading and working in teams associated with design, construction and commissioning of world scale capital projects in both ‘brownfields’ and ‘Greenfields’ scenarios.
Simon Whitlock
Chief Financial Officer
Simon is a qualified accountant (CGMA, CMA, CPA. MAAT) and brings to the team over 20 years of Australian and International experience in a number of key financial roles at both ASX listed and private companies. Simon comes to the team with a strong financial, commercial and business analytical skills combined with proven effective leadership of finance teams. Simon has significant experience in managing working capital requirements of growth businesses with an international footprint. Simon is a member of Southern Guild of Registered Ledger Keepers, Royal College of Business Bookkeepers & Federation of Ledger Practitioners.

Clara Venditti
HR Manager
Clara has more than 10 years’ experience across Oil & Gas, Resources, Engineering, and Finance industries. With general human resources experience, Clara has led strategic and operational HR support and services across recruitment, on boarding, training, remuneration and benefits, employment contract management, career planning and organisational accreditation for 457 visas. Further to this Clara has also managed HR within the M & A environment, through due diligence and post-acquisition integration on both buy and sell sides within the context of global organisations.

Gregory Lane
Project Services & Agency Representative
Project Services and Management expertise with local and international experience in the oil & gas, mining, and utilities industries, as well as a strong understanding within the finance sector. Andrew’s strengths and experience lie in developing and executing business proposals, as well as liaising with external consultants and clients. Possessing competent financial and economic modelling skills and the ability to utilise data for risk and profit based outcomes. Andrew has managed ISO 9001 implementation and ensures that all quality assurance processes are adhered to.
Andrew holds both Bachelor of Commerce and Master of Commerce (Economics & Finance) degrees and is working towards a Master of Science (Energy).

Martin Dunleavy
Director: KVR NT
Andrew has lived in the North of Australia for the last 26 years, bringing valuable local knowledge to the KVR NT office. He has owned and operated his NT services business for 17 years; servicing local and international clients before concentrating and moving into the Oil & Gas and Mining Sector. Andrew has many years of experience in logistics, service and supply, his extensive experience in the NT comes from the following industries: Oil & Gas; Mining; Exploration; Pastoral, Commercial Marine; and Construction.

Trevor Hanlon
Business Development Manager- Queensland
Trevor is a professional civil and mechanical engineer with more than 40 years’ experience in Australia and internationally, across consulting, construction and manufacturing sectors at operational and executive levels. He has held a number of senior executive roles with companies including Rendle Valve Systems, KTV Varnor, and Coastline Transit and has served on a number of industry associations, government committees and private sector boards.

Trevor has broad knowledge and experience in Australian and international business, with an extensive professional network throughout Australia, Asia, Europe and the United States. He has manufactured and supplied products to the oil and gas, petrochemical, power, water, military and nuclear industries.

Page 3: Our Influence
We need the headlines and logos of the following articles and publications:
https://www.tradewirejournal.com.au/article/KVR-buys-Singapore-recruitment-firm?sthash_Q7HkRmWp_tzbe=
http://www.fuelreportdaily.net/storyview.asp?storyID=512847391§ion=Careers+%26+Recruitment§ionsource=s318&aspdsc=yes#.KpdRwtH83MZ.linkedin
http://www.fuelreportdaily.net/storyview.asp?storyID=512847652§ion=Industry+Moves§ionsource=s91&Highlight=kvr&aspdsc=yes
Southern Crude & Fuel Review – this one is getting published soon so just the logo for this one at this time?

Page 4: Who we work with?
Need to have just all logos of the companies that we have worked with. Attached is logos of our clients to match the list below. May need to find better resolution ones.
- Voltrax
- Condor Energy
- Veranta Global
- Fernholt
- PBW – Pelican Boring Worldwide
- Moventa
- Starke Petrol
- Hanbit Fuel Development Company
- Crest
- TQ Group
- LW
- Zephra Rotors
- Orrin Petroleum
- Keta Energy
- Brackwell Alloys Group (BAG)
- Pinnacle Energy
- Tirolo Resources
- Millbrook Meats
- Dorvan
- Hartigan Ledger
- Veshar South Korea
- Kelt Ridge Iron Ore
- Worldwide Utility Holdings
- Falcon Oil
- Tandrel
- Brundle Nickel
- Vintro Oil
- Durvane
- KMT
- Thornbury Alumina

• DIN Offc

• 4 separate pages:
• 1. Menu of Services
• 2. Our Team
• 3. Our Influences (media companies)
• 4. Who we work with
• Keep in colours of KVR and ensure same header/footer used for all 4 pages
• orange = #D76927, R-215 G-105 B-39, CMYK C-11.65 M-70.4 Y-100 K-1.52
• Blue = #21224B, R-33 G-34 B-75, CMYK C-95.65, M-92.65 Y-39.82, K40.01
• Same theme across all 4
• Visually appealing
• Brief information
• Colour
• Images
• Made up information - if unsure please contact us

```html
<!DOCTYPE html>
<html lang="en">
<head>
<meta charset="utf-8">
<title>KVR – Menu of Services &amp; Our Team</title>
<link href="https://fonts.googleapis.com/css2?family=Source+Sans+3:ital,wght@0,400;0,600;0,700;1,400&display=swap" rel="stylesheet">
<style>
  :root {
    --orange: #D76927;
    --navy: #21224B;
    --ink: #3a3a3a;
    --rule: #21224B;
    --bullet: #b5b5b5;
    --backdrop: #e4e4e4;
    --paper: #ffffff;
    --photo-sky: #3f7fb8;
    --photo-suit: #2a3142;
  }
  * { box-sizing: border-box; margin: 0; padding: 0; }
  html, body { width: 1200px; height: 1200px; overflow: hidden; }
  body {
    background: var(--backdrop);
    font-family: "Source Sans 3", "Source Sans Pro", sans-serif;
    color: var(--ink);
    position: relative;
  }
  .sheet {
    position: absolute;
    top: 224px;
    width: 510px;
    height: 721px;
    background: var(--paper);
    box-shadow: 0 2px 10px rgba(0,0,0,0.15);
    overflow: hidden;
  }
  .sheet--services { left: 64px; }
  .sheet--team { left: 632px; }

  .sheet-header .title {
    position: absolute;
    left: 68px;
    top: 30px;
    font-size: 25px;
    font-weight: 600;
    color: var(--navy);
    letter-spacing: 0.3px;
    line-height: 1;
  }
  .sheet--team .sheet-header .title { top: 34px; }
  .sheet-header .rule {
    position: absolute;
    left: 68px;
    top: 66px;
    width: 302px;
    height: 1px;
    background: var(--rule);
  }
  .brand {
    position: absolute;
    left: 376px;
    top: 28px;
    display: flex;
    align-items: center;
    gap: 6px;
    font-size: 32px;
    font-weight: 700;
    color: var(--navy);
    letter-spacing: 2px;
    line-height: 1;
  }
  .brand .dot {
    width: 10px; height: 10px; border-radius: 50%;
    background: var(--orange);
  }

  .services {
    position: absolute;
    left: 68px;
    top: 90px;
    width: 405px;
    list-style: none;
  }
  .service {
    position: relative;
    font-size: 9px;
    line-height: 13px;
    margin-bottom: 10.5px;
  }
  .service::before {
    content: "";
    position: absolute;
    left: -22px;
    top: 3px;
    width: 6px; height: 6px;
    border-radius: 50%;
    background: var(--bullet);
  }
  .service .name {
    font-size: 11.5px;
    color: var(--orange);
  }
  .service .sub { font-size: 9.5px; color: var(--orange); }

  .member {
    position: absolute;
    left: 43px;
    width: 424px;
    display: flex;
    gap: 22px;
  }
  .member .photo {
    flex: none;
    width: 48px; height: 48px;
    margin-top: 0;
    background: linear-gradient(180deg, var(--photo-sky) 0%, #6da2cf 55%, var(--photo-suit) 56%, var(--photo-suit) 100%);
  }
  .member .photo--grey {
    background: linear-gradient(180deg, #b9b9b9 0%, #d4d4d4 55%, #7f8aa0 56%, #5b6883 100%);
  }
  .member .bio-block { width: 354px; }
  .member .name {
    font-size: 11.5px;
    color: var(--orange);
    line-height: 13px;
  }
  .member .role {
    font-size: 8.5px;
    font-style: italic;
    color: var(--ink);
  }
  .member .bio {
    font-size: 8.6px;
    line-height: 12px;
  }

  .sheet-footer .plant {
    position: absolute;
    left: 30px;
    top: 646px;
    width: 53px;
    height: 36px;
    background: var(--navy);
    opacity: 0.9;
  }
  .sheet-footer .band {
    position: absolute;
    left: 0; right: 0;
    top: 682px;
    height: 39px;
    background: var(--navy);
    border-top: 3px solid #d9d9de;
    color: #fff;
    font-size: 9.6px;
    display: flex;
    align-items: center;
    padding-left: 66px;
  }
</style>
</head>
<body>

<section class="sheet sheet--services">
  <header class="sheet-header">
    <h1 class="title">MENU OF SERVICES</h1>
    <div class="rule"></div>
    <div class="brand">KVR<span class="dot"></span></div>
  </header>

  <ul class="services">
    <li class="service"><span class="name">Engineering Design</span> Lorem ipsum dolor sit amet, consectetur adipiscing elit. Integer in lacus fringilla, ultrices sapien bibendum, maximus erat. In efficitur ligula ut velit commodo dapibus.</li>
    <li class="service"><span class="name">Construction Management</span> Lorem ipsum dolor sit amet, consectetur adipiscing elit. Integer in lacus fringilla, ultrices sapien bibendum, maximus erat. In efficitur ligula ut</li>
    <li class="service"><span class="name">Commissioning (Systems, Processes, Resources)</span> Lorem ipsum dolor sit amet, consectetur adipiscing elit. Integer in lacus fringilla, ultrices sapien bibendum, maximus erat.</li>
    <li class="service"><span class="name">Completions Strategy</span> Lorem ipsum dolor sit amet, consectetur adipiscing elit. Integer in lacus fringilla, ultrices sapien bibendum, maximus erat. In efficitur ligula ut velit commodo dapibus.</li>
    <li class="service"><span class="name">Multi-Disciplinary Engineering</span> Lorem ipsum dolor sit amet, consectetur adipiscing elit. Integer in lacus fringilla, ultrices sapien bibendum, maximus erat.</li>
    <li class="service"><span class="name">Multi-Disciplinary Technicians</span> Lorem ipsum dolor sit amet, consectetur adipiscing elit. Integer in lacus fringilla, ultrices sapien bibendum, maximus erat.</li>
    <li class="service"><span class="name">Operations &amp; Maintenance Support</span> Lorem ipsum dolor sit amet, consectetur adipiscing elit. Integer in lacus fringilla, ultrices sapien bibendum, maximus erat. In efficitur ligula ut velit commodo dapibus.</li>
    <li class="service"><span class="name">EX Inspect &amp; Maintain</span> Lorem ipsum dolor sit amet, consectetur adipiscing elit. Integer in lacus fringilla, ultrices sapien bibendum, maximus erat. In efficitur ligula ut velit commodo dapibus. Integer iaculis lacinia mauris, non porttitor turpis scelerisque in.</li>
    <li class="service"><span class="name">On Site Nitrogen Production</span> Lorem ipsum dolor sit amet, consectetur adipiscing elit. Integer in lacus fringilla, ultrices sapien bibendum, maximus erat.</li>
    <li class="service"><span class="name">Water Treatment</span> Lorem ipsum dolor sit amet, consectetur adipiscing elit. Integer in lacus fringilla, ultrices sapien bibendum, maximus erat. In efficitur ligula ut velit commodo dapibus.</li>
    <li class="service"><span class="name">Compact Separation Systems</span> Lorem ipsum dolor sit amet, consectetur adipiscing elit. Integer in lacus fringilla, ultrices sapien bibendum, maximus erat. In efficitur ligula ut velit commodo dapibus. Curabitur ac neque ligula. Vivamus gravida, justo id pharetra consequat.</li>
    <li class="service"><span class="name">Processes to support services</span> Lorem ipsum dolor sit amet, consectetur adipiscing elit. Integer in lacus fringilla, ultrices sapien bibendum, maximus erat. In efficitur ligula ut velit commodo dapibus. Curabitur ac neque ligula. Vivamus gravida, justo id pharetra consequat.</li>
    <li class="service"><span class="name">Technology to improve efficiency and productivity</span> <span class="sub">(Finishline Relay, TW Relay)</span><br>Lorem ipsum dolor sit amet, consectetur adipiscing elit. Integer in lacus fringilla, ultrices sapien bibendum, maximus erat. In efficitur ligula ut velit commodo dapibus.</li>
  </ul>

  <footer class="sheet-footer">
    <div class="plant" role="img" aria-label="Silhouette of processing plant towers and pipework"></div>
    <div class="band">Head Office – Address: Unit 17, 46-48 Marlow Lane, Perth WA 6000 Australia,&nbsp; Phone: +61 8 9371 5086</div>
  </footer>
</section>

<section class="sheet sheet--team">
  <header class="sheet-header">
    <h1 class="title">OUR TEAM</h1>
    <div class="rule"></div>
    <div class="brand">KVR<span class="dot"></span></div>
  </header>

  <article class="member" style="top:92px">
    <div class="photo" role="img" aria-label="Portrait photo of Derek Halvorsen"></div>
    <div class="bio-block">
      <p class="name">Derek Halvorsen, <span class="role">Chief Executive Officer (CEO)</span></p>
      <p class="bio">An extensively experienced and practical executive in the engineering industry with over 20 years’ service, more specifically in the oil and gas sector, since 1988. The experience has been gained through a wide array of projects throughout Australia and Overseas working in the area of Design, System Analysing, Commissioning and Construction before commencing in Business Development and then finally Company Management and Directorships.</p>
    </div>
  </article>

  <article class="member" style="top:188px">
    <div class="photo" role="img" aria-label="Portrait photo of Simon Whitlock"></div>
    <div class="bio-block">
      <p class="name">Simon Whitlock, <span class="role">Chief Financial Officer</span></p>
      <p class="bio">Simon is a qualified accountant (CGMA, CMA, CPA. MAAT) and brings to the team over 20 years of Australian and International experience in a number of key financial roles at both ASX listed and private companies. Simon comes to the team with a strong financial, commercial and business analytical skills combined with proven effective leadership of finance teams. Simon has significant experience in managing working capital requirements of growth businesses with an international footprint.</p>
    </div>
  </article>

  <article class="member" style="top:283px">
    <div class="photo" role="img" aria-label="Portrait photo of Clara Venditti"></div>
    <div class="bio-block">
      <p class="name">Clara Venditti, <span class="role">HR Manager</span></p>
      <p class="bio">Clara has more than 10 years’ experience across Oil &amp; Gas, Resources, Engineering, and Finance industries. With general human resources experience, Clara has led strategic and operational HR support and services across recruitment, on boarding, training, remuneration and benefits, employment contract management, career planning and organisational accreditation for 457 visas. Further to this Clara has also managed HR within the M &amp; A environment, through due diligence and post-acquisition integration on both buy.</p>
    </div>
  </article>

  <article class="member" style="top:379px">
    <div class="photo" role="img" aria-label="Portrait photo of Gregory Lane"></div>
    <div class="bio-block">
      <p class="name">Gregory Lane, <span class="role">Project Services &amp; Agency Representative</span></p>
      <p class="bio">Project Services and Management expertise with local and international experience in the oil &amp; gas, mining, and utilities industries, as well as a strong understanding within the finance sector. Gregory’s strengths and experience lie in developing and executing business proposals, as well as liaising with external consultants and clients. Possessing competent financial and economic modelling skills and the ability to utilise data for risk and profit based outcomes.</p>
    </div>
  </article>

  <article class="member" style="top:475px">
    <div class="photo photo--grey" role="img" aria-label="Portrait photo of Martin Dunleavy"></div>
    <div class="bio-block">
      <p class="name">Martin Dunleavy, <span class="role">Director: KVR NT</span></p>
      <p class="bio">Martin has lived in the North of Australia for the last 26 years, bringing valuable local knowledge to the KVR NT office. He has owned and operated his NT services business for 17 years; servicing local and international clients before concentrating and moving into the Oil &amp; Gas and Mining Sector. Martin has many years of experience in logistics, service and supply, his extensive experience in the NT comes from the following industries: Oil &amp; Gas; Mining; Exploration; Pastoral, Commercial Marine; and Construction.</p>
    </div>
  </article>

  <article class="member" style="top:572px">
    <div class="photo photo--grey" role="img" aria-label="Portrait photo of Trevor Hanlon"></div>
    <div class="bio-block">
      <p class="name">Trevor Hanlon, <span class="role">Business Development Manager- Queensland</span></p>
      <p class="bio">Trevor is a professional civil and mechanical engineer with more than 40 years’ experience in Australia and internationally, across consulting, construction and manufacturing sectors at operational and executive levels. He has held a number of senior executive roles with companies including Rendle Valve Systems, KTV Varnor, and Coastline Transit and has served on a number of industry associations, government committees and private sector boards.</p>
    </div>
  </article>

  <footer class="sheet-footer">
    <div class="plant" role="img" aria-label="Silhouette of processing plant towers and pipework"></div>
    <div class="band">Head Office – Address: Unit 17, 46-48 Marlow Lane, Perth WA 6000 Australia,&nbsp; Phone: +61 8 9371 5086</div>
  </footer>
</section>

</body>
</html>
```